Oak Bend Diesel & Trailer Repair needs a logo and business cards*

We need a logo design and cards for a new business in Willowmere, TS called Oak Bend Diesel & Trailer Repair. I would like a design with a Hallorway or Drummoke Semi on it and a gray background card with maybe red and white writing. Address is 517 Marsh Hollow Road Willowmere, TS 31884 phone is 229-555-0147 Wesley Hardcastle 229-555-0182, Danny Whitlow 229-555-0163 email address oakbenddieselandtrailer@mailexample.net offic enumber is 229-555-0147

Target Market(s)

people needing truck repairs

Logo Text

Oak Bnd Diesel & Trailer Repair

Logo styles of interest
Wordmark Logo
Font styles to use
Serif
Sans Serif

Colors

Designer to choose colors to be used in the design.

Requirements
Must have
• names, address, phone number, email address and a picture of a Hallorway or Drummoke Semi
• i attached a picture of a card that I would like a card similar to
Nice to have
• i would like it it double sided- on the back i want
• We specialize in DOT inspections, Preventative maintenance, Brake repair, Clutch repair, tire repair, on and off site diagnostics, service calls
• Trailer repair

```html
<!DOCTYPE html>
<html lang="en">
<head>
<meta charset="utf-8">
<title>Oak Bend Diesel &amp; Trailer Repair – Business Card</title>
<link rel="stylesheet" href="https://fonts.googleapis.com/css2?family=Jost:wght@500;600&display=swap">
<style>
  :root {
    --page-bg: #e9e8e9;
    --card-bg: #333333;
    --brand-red: #e8242b;
    --ink-white: #ffffff;
    --truck-red-light: #d9353a;
    --truck-red-dark: #8e1418;
  }
  * { margin: 0; padding: 0; box-sizing: border-box; }
  html, body {
    width: 1200px;
    height: 612px;
    overflow: hidden;
    background: var(--page-bg);
    font-family: "Jost", sans-serif;
  }
  .canvas {
    position: relative;
    width: 1200px;
    height: 612px;
  }
  .business-card {
    position: absolute;
    left: 100px;
    top: 30px;
    width: 1000px;
    height: 552px;
    background: var(--card-bg);
    overflow: hidden;
    text-transform: uppercase;
    color: var(--ink-white);
  }
  .card-swooshes {
    position: absolute;
    inset: 0;
    width: 100%;
    height: 100%;
  }
  .contact {
    position: absolute;
    font-weight: 500;
    font-size: 25px;
    line-height: 32px;
    letter-spacing: 0.2px;
    white-space: nowrap;
  }
  .contact .phone { color: var(--brand-red); display: block; }
  .contact-left { left: 51px; top: 44px; }
  .contact-right { right: 32px; top: 38px; text-align: left; }
  .brand-name {
    position: absolute;
    left: 318px;
    top: 98px;
    width: 370px;
    font-weight: 600;
    font-size: 33px;
    line-height: 38px;
    color: var(--ink-white);
    text-align: center;
  }
  .truck-photo {
    position: absolute;
    left: 106px;
    top: 252px;
    width: 334px;
    height: 218px;
  }
  .office-info {
    position: absolute;
    right: 32px;
    top: 358px;
    text-align: right;
    font-weight: 500;
    white-space: nowrap;
  }
  .office-line { font-size: 26px; line-height: 40px; }
  .office-line .phone { color: var(--brand-red); }
  .address { font-size: 22px; line-height: 30px; margin-top: 8px; }
  .email {
    font-size: 24px;
    line-height: 34px;
    margin-top: 10px;
    text-transform: none;
  }
</style>
</head>
<body>
<main class="canvas">
  <section class="business-card">
    <svg class="card-swooshes" viewBox="0 0 1000 552" preserveAspectRatio="none" aria-hidden="true">
      <path fill="var(--brand-red)" d="M0 450 C 260 470, 520 380, 1000 170 L 1000 248 C 700 330, 420 420, 0 466 Z"/>
      <path fill="var(--ink-white)" d="M0 530 C 160 490, 400 330, 760 265 C 860 250, 940 248, 1000 250 L 1000 268 C 820 270, 560 310, 330 430 C 200 490, 80 530, 0 550 Z"/>
    </svg>

    <div class="contact contact-left">
      Danny Whitlow
      <span class="phone">229-555-0163</span>
    </div>

    <div class="contact contact-right">
      Wesley Hardcastle
      <span class="phone">229-555-0182</span>
      <span class="phone">229-555-0147</span>
    </div>

    <h1 class="brand-name">Oak Bnd Diesel &amp; Trailer Repair</h1>

    <svg class="truck-photo" viewBox="0 0 334 218" role="img" aria-label="Photo of a red Hallorway semi tractor truck">
      <defs>
        <linearGradient id="truckTone" x1="0" y1="0" x2="1" y2="1">
          <stop offset="0" stop-color="var(--truck-red-light)"/>
          <stop offset="1" stop-color="var(--truck-red-dark)"/>
        </linearGradient>
      </defs>
      <rect x="0" y="0" width="334" height="218" rx="14" fill="url(#truckTone)"/>
    </svg>

    <div class="office-info">
      <p class="office-line">Office : <span class="phone">229-555-0147</span></p>
      <p class="address">517 Marsh Hollow Road<br>Willowmere, TS 31884</p>
      <p class="email">oakbenddieselandtrailer@mailexample.net</p>
    </div>
  </section>
</main>
</body>
</html>
```